Design Business Card CORAL TIDE MOWING

We have attached a copy of our Logo, we like a business card designed with logo and mobile phone number on one side that stands out maybe gloss and on the other side it can have the services we do small picture of our logo name number, I have attached an idea to this that I have seen online, this is a business owned by a woman so we like pinks black and navy
Our logo is attached in pdf
Target Market(s)
Home owners that need lawns mowed
Industry/Entity Type
Lawns and gardens
Contact Information for Business Card
Logo business Owner name Dorinda Pask mobile number 0417296054
Font styles to use
Look and feel
Each slider illustrates characteristics of the customer's brand and the style your logo design should communicate.

```html
<!DOCTYPE html>
<html lang="en">
<head>
<meta charset="utf-8">
<title>Coral Tide Mowing – Business Card</title>
<link href="https://fonts.googleapis.com/css2?family=Bebas+Neue&display=swap" rel="stylesheet">
<style>
  :root {
    --stage: #e9e9ec;
    --pink: #d42a86;
    --pink-light: #e566a8;
    --ink: #1c1a1d;
    --white: #ffffff;
    --green: #39b54a;
  }
  * { margin: 0; padding: 0; box-sizing: border-box; }
  html, body {
    width: 1200px; height: 939px; overflow: hidden;
    background: var(--stage);
    font-family: "Bebas Neue", "Arial Narrow", sans-serif;
  }
  .stage {
    position: relative; width: 1200px; height: 939px;
  }
  .card {
    position: absolute; left: 290px; width: 620px; height: 354px;
    box-shadow: 0 10px 30px rgba(0,0,0,.18);
    display: flex; flex-direction: column; align-items: center; justify-content: center;
    text-align: center;
  }
  .card--front {
    top: 70px;
    background: radial-gradient(ellipse at 45% 40%, var(--pink-light) 0%, var(--pink) 80%);
  }
  .card--back {
    top: 515px;
    background: var(--white);
  }
  .brand {
    display: flex; align-items: center; gap: 14px;
    color: var(--ink);
  }
  .brand__dot {
    width: 46px; height: 46px; border-radius: 50%; background: var(--ink);
  }
  .card--back .brand__dot { background: var(--pink); width: 38px; height: 38px; }
  .brand__name { font-size: 54px; letter-spacing: 1px; line-height: 1; }
  .card--back .brand__name { font-size: 44px; }
  .front-call {
    margin-top: 48px; font-size: 30px; letter-spacing: 2px; color: var(--ink);
  }
  .services {
    margin-top: 26px; font-size: 19px; letter-spacing: 1px; color: var(--ink); line-height: 1.15;
  }
  .services .sep { color: var(--pink); padding: 0 4px; }
  .owner-name {
    margin-top: 14px; font-size: 38px; letter-spacing: 2px; color: var(--pink); line-height: 1;
  }
  .owner-role { font-size: 18px; letter-spacing: 1px; color: var(--ink); }
  .phone {
    margin-top: 8px; display: flex; align-items: center; gap: 8px;
    font-size: 28px; letter-spacing: 2px; color: var(--ink);
  }
  .phone svg { width: 22px; height: 22px; }
</style>
</head>
<body>
<main class="stage">
  <section class="card card--front" aria-label="Business card front">
    <div class="brand">
      <span class="brand__dot"></span>
      <span class="brand__name">CORAL TIDE MOWING</span>
    </div>
    <p class="front-call">CALL: 0417296054</p>
  </section>

  <section class="card card--back" aria-label="Business card back">
    <div class="brand">
      <span class="brand__dot"></span>
      <span class="brand__name">CORAL TIDE MOWING</span>
    </div>
    <p class="services">
      GARDEN MAINTENANCE<span class="sep">|</span>RUBBISH REMOVAL<span class="sep">|</span>TRIMMING<br>
      WEEDING<span class="sep">|</span>LAWN CARE
    </p>
    <p class="owner-name">DORINDA PASK</p>
    <p class="owner-role">OWNER</p>
    <p class="phone">
      <svg viewBox="0 0 24 24" aria-hidden="true">
        <path fill="var(--green)" d="M6.6 10.8a15.1 15.1 0 0 0 6.6 6.6l2.2-2.2a1 1 0 0 1 1-.25 11.4 11.4 0 0 0 3.6.57 1 1 0 0 1 1 1V20a1 1 0 0 1-1 1A17 17 0 0 1 3 4a1 1 0 0 1 1-1h3.5a1 1 0 0 1 1 1c0 1.25.2 2.45.57 3.57a1 1 0 0 1-.25 1z"/>
      </svg>
      0417296054
    </p>
  </section>
</main>
</body>
</html>
```